Business Card Design

I would like a new business card design for an accounting firm that specializes in resolving clients tax problems. I want the card to give the impression that we are not your typical stodgy accounting firm, but at the same time we will get the job done.
Industry/Entity Type
Business
Contact Information for Business Card
Marcus T Kelbeck
Certified Public Accountant
27-08 63rd Avenue
Sunnyside, NY 11104
Tel: (718) 555-0143
Fax: (888) 555-0176
e-mail: mtkledger@quillpost.net
website: harborstonefiscalaidgroup.com

```html
<!DOCTYPE html>
<html lang="en">
<head>
<meta charset="utf-8">
<title>Marcus T Kelbeck — Business Card</title>
<link rel="stylesheet" href="https://fonts.googleapis.com/css2?family=Jost:wght@400;500&family=Tinos:wght@400;700&display=swap">
<style>
  :root {
    --card-bg: #121314;
    --brand-blue: #0a7cc1;
    --text-white: #ffffff;
    --key-grey: #3d4043;
    --key-dark: #141517;
    --key-border: #a9abad;
  }
  html, body {
    margin: 0;
    padding: 0;
    overflow: hidden;
    background: var(--card-bg);
  }
  .card {
    position: relative;
    width: 704px;
    height: 1200px;
    background: var(--card-bg);
    overflow: hidden;
    font-family: "Tinos", "Times New Roman", serif;
    color: var(--text-white);
  }
  .name {
    position: absolute;
    left: 55px;
    top: 52px;
    margin: 0;
    font-family: "Jost", "Futura", sans-serif;
    font-weight: 400;
    font-size: 56px;
    line-height: 1;
    color: var(--brand-blue);
    white-space: nowrap;
  }
  .title {
    position: absolute;
    left: 150px;
    top: 124px;
    margin: 0;
    font-size: 24px;
    line-height: 1;
    white-space: nowrap;
  }
  .contact {
    position: absolute;
    left: 81px;
    top: 338px;
    margin: 0;
    list-style: none;
    padding: 0;
    white-space: nowrap;
  }
  .contact li { line-height: 1; }
  .contact .phone { font-size: 33px; margin-bottom: 7px; }
  .contact .fax { font-size: 33px; margin-bottom: 10px; }
  .contact .email { font-size: 28px; margin-bottom: 9px; }
  .contact .web { font-size: 28px; margin-bottom: 9px; }
  .contact .address { font-size: 27px; color: var(--brand-blue); }

  .keypad {
    position: absolute;
    left: 53px;
    top: 555px;
    display: grid;
    grid-template-columns: 140px 140px 140px 140px;
    grid-template-rows: 90px 90px 91px 90px 90px 96px;
    column-gap: 12px;
    row-gap: 14px;
  }
  .key {
    display: flex;
    align-items: center;
    justify-content: center;
    box-sizing: border-box;
    background: var(--key-grey);
    font-weight: 700;
    font-size: 31px;
    color: var(--text-white);
  }
  .key--digit {
    background: var(--key-dark);
    border: 2px solid var(--key-border);
  }
  .key--equals {
    background: var(--brand-blue);
  }
</style>
</head>
<body>
  <main class="card">
    <h1 class="name">Marcus T Kelbeck</h1>
    <p class="title">Certified Public Accountant</p>

    <ul class="contact">
      <li class="phone">Tel : (718) 555-0143</li>
      <li class="fax">Fax:(888) 555-0176</li>
      <li class="email">E-Mail : mtkledger@quillpost.net</li>
      <li class="web">www : harborstonefiscalaidgroup.com</li>
      <li class="address">27-08, 63RD Avenue, sunny side, NY 11104.</li>
    </ul>

    <div class="keypad">
      <div class="key">MC</div>
      <div class="key">MR</div>
      <div class="key">MS</div>
      <div class="key">M+</div>

      <div class="key">C</div>
      <div class="key">±</div>
      <div class="key">%</div>
      <div class="key">÷</div>

      <div class="key key--digit">7</div>
      <div class="key key--digit">8</div>
      <div class="key key--digit">9</div>
      <div class="key">X</div>

      <div class="key key--digit">4</div>
      <div class="key key--digit">5</div>
      <div class="key key--digit">6</div>
      <div class="key">-</div>

      <div class="key key--digit">1</div>
      <div class="key key--digit">2</div>
      <div class="key key--digit">3</div>
      <div class="key">+</div>

      <div class="key key--digit"></div>
      <div class="key">0</div>
      <div class="key">.</div>
      <div class="key key--equals">=</div>
    </div>
  </main>
</body>
</html>
```